Tattoo Artist needs a personal business card designed

I am looking for a classy, clean, but antique feeling business card for myself that matches the theme and vibe of my tattoo shop. I would like to see a couple different options but we can go with an all black background, to start. I would like to see some western metallic lettering and deep/dark red accents. Maybe try adding a few with a mix of white fonts too. I would like to see the Shop's name and location which is Crane Voltage Ink, 4382 W. Delmora Ave. Tampa FL. 33617 Our tattoo shop has a western antique vibe, yet its classy and professional. We have a website you can see the color scheme and grab anymore information for designing this business card from: www.cranevoltageink.example - and if you want to add the website to the card. I would like my personal IG handle somewhere small with a unique and cleaner IG logo next to the name. My IG handle is: @tessadrillinkwork I am basically trying to look for multiple ideas/concepts that will match best with our website and sticker. (Which I will upload in the files) I would like it to be very clean, simple, classy, but have a western traditional tattooing feel to it. Like an antique stores business card. Add whatever information you think would be best, since I am not the professional graphic designer.
Shop Name: Crane Voltage Ink
Location: 4382 W Delmora Ave Tampa FL 33617
Website: www.cranevoltageink.example
Number: 813 555 0172
My Personal IG: @tessadrillinkwork

Thank you for taking your time to help me out with this project. Afterwards, I might need our studios website up for re-designing! So my end goal is to make everything intergraded with one another. I more likely need a logo too.

Target Market(s)

Professionals 35-55 years of age Male and Female
Firefighters, Military Service men and women

Contact Information for Business Card

All black background, with golden and red accents.
Traditional style, cowboy, western. Sharp, Clean, and Classy.

Requirements
Must have
• Shop Name - Crane Voltage Ink
• Shop Location - 4382 W Delmora Ave Tampa FL 33617
• My Name - Tessa Drill
• UNIQUE IG LOGO along with My Instagram - @tessadrillinkwork
• Number - 813 555 0172
Nice to have
• Gold metallic font
• Red accents
• Western Antique Oddity feel
• Might be nice to have the Website if it can work and fit in the space.

```html
<!DOCTYPE html>
<html lang="en">
<head>
<meta charset="utf-8">
<title>Tessa Drill – Business Card</title>
<link rel="stylesheet" href="https://fonts.googleapis.com/css2?family=Lato:wght@400;700&display=swap">
<style>
  :root {
    --backdrop: #1c1c1c;
    --card: #232323;
    --card-edge: #2b2b2b;
    --gold: #b8903a;
    --white: #f2f2f2;
    --muted-line: #3a3a3a;
  }
  * { box-sizing: border-box; margin: 0; padding: 0; }
  html, body {
    width: 1200px; height: 900px; overflow: hidden;
    background: var(--backdrop);
    font-family: "Lato", sans-serif;
  }
  .sheet {
    width: 1200px; height: 900px;
    display: flex; flex-direction: column;
    align-items: center; justify-content: center; gap: 40px;
  }
  .card {
    position: relative;
    width: 630px; height: 360px;
    background: linear-gradient(135deg, var(--card-edge), var(--card));
    border-bottom: 5px solid var(--gold);
    display: flex; align-items: center;
  }
  .shop-name {
    color: var(--gold);
    font-weight: 700;
    font-size: 30px;
    letter-spacing: 2px;
    text-transform: uppercase;
    text-align: center;
    line-height: 1.2;
  }
  .card--front { justify-content: center; }
  .card--back { padding: 0 40px 0 50px; }
  .card--back .brand { width: 230px; }
  .card--back .brand .shop-name { font-size: 24px; }
  .divider {
    width: 2px; height: 170px; background: var(--gold);
    margin: 0 28px 0 30px;
  }
  .details { color: var(--white); font-size: 16px; line-height: 1.5; }
  .artist-name {
    color: var(--gold);
    font-weight: 700;
    font-size: 26px;
    letter-spacing: 3px;
    text-transform: uppercase;
    margin-bottom: 8px;
  }
  .address { margin-bottom: 8px; }
  .contact-list { list-style: none; }
  .contact-list li { display: flex; align-items: center; gap: 10px; }
  .contact-list svg { width: 14px; height: 14px; flex: none; }
</style>
</head>
<body>
<main class="sheet">
  <section class="card card--front">
    <div class="shop-name">Crane Voltage Ink</div>
  </section>

  <section class="card card--back">
    <div class="brand"><div class="shop-name">Crane Voltage Ink</div></div>
    <div class="divider"></div>
    <div class="details">
      <h1 class="artist-name">Tessa Drill</h1>
      <p class="address">4382 W Delmora Ave<br>Tampa FL 33617</p>
      <ul class="contact-list">
        <li>
          <svg viewBox="0 0 14 14" fill="none" stroke="var(--gold)" stroke-width="1.4" stroke-linejoin="round"><path d="M3 1.5 L5 4 L4 5.5 Q5.5 8.5 8.5 10 L10 9 L12.5 11 L11 12.8 Q5 12 1.5 3 Z"/></svg>
          813 555 0172
        </li>
        <li>
          <svg viewBox="0 0 14 14" fill="none" stroke="var(--gold)" stroke-width="1.3"><rect x="1" y="3" width="12" height="8"/><path d="M1 3 L7 8 L13 3"/></svg>
          @tessadrillinkwork
        </li>
        <li>
          <svg viewBox="0 0 14 14" fill="none" stroke="var(--gold)" stroke-width="1.1"><circle cx="7" cy="7" r="5.8"/><ellipse cx="7" cy="7" rx="2.6" ry="5.8"/><path d="M1.2 7 H12.8 M2 4 H12 M2 10 H12"/></svg>
          www.cranevoltageink.example
        </li>
        <li>
          <svg viewBox="0 0 14 14"><rect x="1.5" y="1.5" width="11" height="11" fill="var(--gold)"/></svg>
          @tessadrillinkwork
        </li>
      </ul>
    </div>
  </section>
</main>
</body>
</html>
```